Brochure Design

Looking for designer to make a brochure (2 sided) similar to attached pdf. Will provide the details and graphics needed. PDF is similar style to what we want. PPT has new content.

```html
<!DOCTYPE html>
<html lang="en">
<head>
<meta charset="utf-8">
<title>Lingofield Brochure</title>
<link rel="stylesheet" href="https://fonts.googleapis.com/css2?family=Oswald:wght@700&family=Roboto:wght@400;700&display=swap">
<style>
  :root {
    --red: #d9141b;
    --ink: #2a2a2a;
    --paper: #ffffff;
    --backdrop: #eeeeee;
    --city-light: #d8d3cc;
    --city-mid: #b9b2a8;
    --city-dark: #8f887f;
  }
  * { box-sizing: border-box; margin: 0; padding: 0; }
  html, body { width: 686px; height: 1200px; overflow: hidden; }
  body {
    background: var(--backdrop);
    font-family: "Roboto", Arial, sans-serif;
    position: relative;
  }
  .page {
    position: absolute;
    left: 92px;
    width: 506px;
    height: 565px;
    box-shadow: 0 2px 6px rgba(0,0,0,0.18);
    overflow: hidden;
  }
  .page--front { top: 34px; background: var(--paper); }
  .page--back  { top: 636px; height: 530px; background: var(--red); }

  .front-header {
    background: var(--red);
    height: 103px;
    padding: 22px 26px 0;
  }
  .front-title {
    font-family: "Oswald", "Arial Narrow", sans-serif;
    font-weight: 700;
    color: #fff;
    font-size: 26px;
    line-height: 31px;
    text-transform: uppercase;
    letter-spacing: 0.3px;
  }
  .front-body {
    padding: 24px 26px 0;
    color: var(--ink);
    font-size: 9px;
    line-height: 13px;
  }
  .front-body p { margin-bottom: 9px; }
  .front-body .lead { font-weight: 700; }
  .front-body strong { font-weight: 700; }

  .city-visual {
    position: absolute;
    left: 0; right: 0; bottom: 0;
    height: 245px;
    background: linear-gradient(180deg, var(--paper) 0%, var(--city-light) 22%, var(--city-mid) 60%, var(--city-dark) 100%);
  }

  .back-copy {
    position: absolute;
    left: 30px;
    right: 30px;
    top: 48px;
    color: #fff;
    font-size: 9.4px;
    line-height: 13.6px;
    text-align: justify;
  }
  .back-copy p { display: inline; }
</style>
</head>
<body>

  <section class="page page--front">
    <header class="front-header">
      <h1 class="front-title">Lingofield:<br>Decode the real message</h1>
    </header>
    <div class="front-body">
      <p class="lead">No More Robotic Translations—Get Down and Dirty with Real Language</p>
      <p>Forget stiff, lifeless translations. Our AI-powered system translates <strong>slang, typos, emojis, abbreviations, local dialects, and hidden meanings</strong>—so nothing gets lost in translation!</p>
      <p>Whether it's <strong>text messages, recorded calls, social media posts, or street slang</strong>, Lingofield analyzes language like real people use it—<strong>raw, unfiltered, and full of nuance.</strong> We work across <strong>70+ languages</strong>, ensuring you don't just get the words—you get the real intent behind them.</p>
      <p>Because in an investigation, <strong>understanding the truth can mean the difference between a lead and a dead end.</strong></p>
      <p>What's up, dude? "got the package in the fridge, real cool and no bumps." This is no fake or junk, it's pure stuff for the high rollers. If you're up for the game, let me know before they swipe it. But you know, no nonsense, the heat is on and the eyes are on the prowl. You come up with the dough and we make the deal clean, alright?</p>
    </div>
    <div class="city-visual" role="img" aria-label="Aerial photo of a city with a large red location pin marking a spot"></div>
  </section>

  <section class="page page--back">
    <div class="back-copy">
      <p>Lingofield: The Future of Translation. Break language barriers with precision. Traditional translation tools miss what matters most: context, tone and intent. Our engine reads a message the way a native speaker would, catching slang, shorthand, regional idioms, misspellings and coded phrasing that standard software flattens or ignores. Every result arrives with a plain summary, a literal rendering and notes on tone, so analysts can see both what was said and what was meant. </p>
      <p>Built for investigators, compliance teams and field officers, Lingofield processes chat logs, voice recordings, transcripts, screenshots and social posts in more than seventy languages. Audio is transcribed, cleaned of noise and matched to speakers before translation begins. Emojis and abbreviations are decoded in context, and recurring terms are tracked across an entire case file so patterns stay visible from the first message to the last. </p>
      <p>Why it matters: a single misread word can send an inquiry in the wrong direction. A phrase that looks harmless in a dictionary may carry a very different meaning on the street, in a specific neighbourhood or inside a closed group. Lingofield flags these moments, explains the likely reading and rates its confidence, giving your team the clarity to act quickly and the evidence to back every decision. </p>
      <p>Key features: real language detection for slang, dialect and code switching; sentiment and intent scoring; speaker separation for multi-party calls; secure, audited workspaces with role-based access; exportable reports ready for court or review; and continuous updates as new terms appear online and offline. </p>
      <p>Security comes first. All material stays encrypted in transit and at rest, nothing is used to train public models, and every action is logged for full chain of custody. Deploy in our protected cloud or on your own servers, with support from specialists who understand both linguistics and investigative work. </p>
      <p>From a single urgent message to thousands of hours of intercepted audio, Lingofield scales with your caseload. Upload, review and share findings in minutes instead of days, and keep every translation linked to its source for easy verification. </p>
      <p>Stop guessing what people really mean. Start understanding them. Contact our team today to arrange a guided demonstration and see how real language translation can move your next case forward.</p>
    </div>
  </section>

</body>
</html>
```